Modern Business Card Design
Consulting firm - Engineering/Infrastructure Sector
Use same font as used in my logo
but we are open to new fonts, as long as the printer will not have trouble with them.
Professional
Melanie Trovaskis
Partner
4215 Linwood Avenue
Suite 207
mtrovaskis@brightholmpx.com
www.brightholmpx.com
we're looking for something sharp and complementary to our logo

```html
<!DOCTYPE html>
<html lang="en">
<head>
<meta charset="utf-8">
<title>Brightholm Business Card</title>
<link href="https://fonts.googleapis.com/css2?family=Cormorant+Garamond:wght@500;600&display=swap" rel="stylesheet">
<style>
  :root {
    --page-bg: #e9e9ec;
    --card-white: #ffffff;
    --brand-navy: #1b3182;
    --band-navy: #1b3182;
    --accent-sky: #5fa8e0;
    --text-white: #ffffff;
    --text-soft: #c9d3ef;
  }
  * { margin: 0; padding: 0; box-sizing: border-box; }
  html, body {
    width: 1200px; height: 900px; overflow: hidden;
    background: var(--page-bg);
    font-family: "Cormorant Garamond", "Georgia", serif;
  }
  .card {
    position: absolute; left: 100px; top: 164px;
    width: 1000px; height: 572px;
    background: var(--card-white);
    box-shadow: 0 10px 30px rgba(0,0,0,0.18);
    overflow: hidden;
  }
  .brand {
    position: absolute; left: 400px; top: 118px;
    display: flex; align-items: center; gap: 18px;
  }
  .brand-square {
    width: 26px; height: 26px;
    background: var(--accent-sky);
  }
  .brand-name {
    font-size: 60px; font-weight: 600; letter-spacing: 1px;
    color: var(--brand-navy); line-height: 1;
  }
  .info-band {
    position: absolute; left: 0; top: 272px;
    width: 100%; height: 252px;
    background: var(--band-navy);
  }
  .name-tab {
    position: absolute; left: 0; top: 118px;
    width: 14px; height: 62px;
    background: var(--accent-sky);
  }
  .person {
    position: absolute; left: 34px; top: 120px;
    color: var(--text-white);
  }
  .person-name { font-size: 32px; font-weight: 600; letter-spacing: 0.5px; line-height: 1.1; }
  .person-role { font-size: 17px; font-weight: 500; color: var(--text-soft); margin-top: 4px; letter-spacing: 1px; }
  .contact-list {
    position: absolute; left: 562px; top: 16px;
    list-style: none; color: var(--text-white);
    font-size: 20px; font-weight: 600; line-height: 30px; letter-spacing: 0.5px;
    text-transform: uppercase;
  }
  .contact-list li { display: flex; align-items: center; gap: 10px; }
  .contact-list li.indent { padding-left: 30px; }
  .contact-icon { width: 20px; height: 20px; flex: none; }
</style>
</head>
<body>
  <main class="card">
    <div class="brand">
      <span class="brand-square"></span>
      <span class="brand-name">Brightholm</span>
    </div>

    <section class="info-band">
      <span class="name-tab"></span>
      <div class="person">
        <div class="person-name">Melanie Trovaskis</div>
        <div class="person-role">Partner</div>
      </div>

      <ul class="contact-list">
        <li>
          <svg class="contact-icon" viewBox="0 0 20 20"><circle cx="10" cy="10" r="10" fill="#fff"/><path d="M10 4a4 4 0 0 0-4 4c0 3 4 8 4 8s4-5 4-8a4 4 0 0 0-4-4z" fill="#1b3182"/><circle cx="10" cy="8" r="1.5" fill="#fff"/></svg>
          4215 Linwood Avenue
        </li>
        <li class="indent">Suite 207</li>
        <li>
          <svg class="contact-icon" viewBox="0 0 20 20"><circle cx="10" cy="10" r="10" fill="#fff"/><rect x="7" y="4" width="6" height="12" rx="1.2" fill="#1b3182"/></svg>
          4105550182
        </li>
        <li>
          <svg class="contact-icon" viewBox="0 0 20 20"><circle cx="10" cy="10" r="10" fill="#fff"/><path d="M6 5l2.5-.5 1.3 3-1.6 1.2a7 7 0 0 0 3 3l1.2-1.6 3 1.3L15 14c-5 0-9-4-9-9z" fill="#1b3182"/></svg>
          4105550297
        </li>
        <li>
          <svg class="contact-icon" viewBox="0 0 20 20"><circle cx="10" cy="10" r="10" fill="#fff"/><rect x="5" y="6" width="10" height="8" fill="#1b3182"/><rect x="6.5" y="7.5" width="7" height="3" fill="#fff"/></svg>
          4105550346
        </li>
        <li>
          <svg class="contact-icon" viewBox="0 0 20 20"><circle cx="10" cy="10" r="10" fill="#fff"/><rect x="4.5" y="6" width="11" height="8" fill="#1b3182"/><path d="M4.5 6l5.5 4.5L15.5 6" fill="none" stroke="#fff" stroke-width="1"/></svg>
          mtrovaskis@brightholmpx.com
        </li>
        <li>
          <svg class="contact-icon" viewBox="0 0 20 20"><circle cx="10" cy="10" r="10" fill="#fff"/><circle cx="10" cy="10" r="5.5" fill="none" stroke="#1b3182" stroke-width="1.4"/><ellipse cx="10" cy="10" rx="2.3" ry="5.5" fill="none" stroke="#1b3182" stroke-width="1.2"/><line x1="4.5" y1="10" x2="15.5" y2="10" stroke="#1b3182" stroke-width="1.2"/></svg>
          www.brightholmpx.com
        </li>
      </ul>
    </section>
  </main>
</body>
</html>
```